New look modernised front page for Marlowe Lawn Sports Guild Website Which incorporates our new logo (to be provided as a png file)
We want the home page to a panel to allow an image rotator and provide ready access to links to other inflation via some link menus/panel/button
1. Join a Croquet Club - links to details about Croquet in NSW - gateway to information of interest or the general public/“interested others” eg about the game, clubs locations and contacts
2. Club and Member Information - newsletters, Calender of events, and downloads
3. Officials and volunteers - training resources etc
4. Member and Club sign in - access to database
5. About Us - information about Marlowe Lawn Sports Guild incorporated -peak body for croquet in NSW - governance, contact details etc

Current website is at https://www.marlowe-guild.org/index.html

Target Market(s)

Dual target - People interested in learning about croquet and existing members

Number of Pages Required

1 page

Font styles to use
Sans Serif

Colors
0255a3
3377b5
85acd3
85cae6
33a6d7
0792cd
00a990

Requirements
Must have
• Contemporary feel
• Include logo - file attached
• Colours to include blues which are the NSW colour
Nice to have
• We want the home page to a panel to allow an image rotator and provide ready access to links to other inflation via some link menus/panel/button
• 1. Join a Croquet Club - links to details about Croquet in NSW - gateway to information of interest or the general public/“interested others” eg about the game, clubs locations and contacts
• 2. Club and Member Information - newsletters, Calender of events, and downloads
• 3. Officials and volunteers - training resources etc
• 4. Member and Club sign in - access to database
• 5. About Us - information about Marlowe Lawn Sports Guild incorporated -peak body for croquet in NSW - governance, contact details etc
• Want to have feeling of activity/movement/alive
• Current website is at https://www.marlowe-guild.org/index.html
• Some photos attached for information

```html
<!DOCTYPE html>
<html lang="en">
<head>
<meta charset="utf-8">
<title>Marlowe Lawn Sports Guild</title>
<link rel="stylesheet" href="https://fonts.googleapis.com/css2?family=Montserrat:wght@400;500;600;700&family=Open+Sans:wght@400;600&display=swap">
<style>
:root{
  --teal:#17a086;
  --teal-dark:#128a73;
  --navy:#0d4a9c;
  --royal:#0255a3;
  --sky:#0792cd;
  --ink:#333;
  --muted:#666;
  --line:#e3e3e3;
  --paper:#fff;
  --mist:#f6f7f8;
  --coal:#262626;
}
*{box-sizing:border-box;margin:0;padding:0}
html,body{width:1200px;height:2995px;overflow:hidden}
body{font-family:"Open Sans",Arial,sans-serif;color:var(--ink);background:var(--paper)}
.canvas{position:relative;width:1200px;height:2995px}
section,header,footer{position:absolute;left:0;width:1200px}
h2,h3,h4,.brand,.nav a,.btn{font-family:"Montserrat",Arial,sans-serif}

/* header */
.site-header{top:0;height:90px;background:var(--teal);display:flex;align-items:center;padding:0 86px}
.brand{display:flex;align-items:center;gap:10px;color:#fff;font-weight:700;font-size:16px;letter-spacing:.5px}
.brand-dot{width:14px;height:14px;border-radius:50%;background:#fff}
.nav{margin-left:auto;display:flex;align-items:center;gap:28px}
.nav a{color:#fff;text-decoration:none;font-size:12px;font-weight:600}
.nav .join{border:1.5px solid #fff;padding:11px 9px}

/* hero */
.hero{top:90px;height:522px;background:linear-gradient(180deg,#4e5f3e 0%,#7b7a63 45%,#9c9a8c 100%)}
.hero .photo{position:absolute;inset:0;background:linear-gradient(90deg,rgba(30,40,25,.35),rgba(120,110,80,.15),rgba(30,40,25,.35))}
.hero-copy{position:absolute;left:0;right:0;top:296px;text-align:center;color:#fff}
.hero-copy h1{font-family:"Montserrat",Arial,sans-serif;font-weight:700;font-size:36px;letter-spacing:.5px}
.hero-copy p{font-size:22px;margin-top:16px;letter-spacing:.3px}
.btn{display:inline-block;color:#fff;text-decoration:none;font-size:14px;font-weight:500}
.hero .btn{margin-top:20px;background:var(--royal);width:194px;height:48px;line-height:48px}

/* about */
.about{top:612px;height:388px}
.about h2{position:absolute;left:86px;top:82px;color:var(--teal);font-size:22px;font-weight:600;letter-spacing:.5px}
.about p{position:absolute;left:86px;top:130px;width:456px;font-size:11.5px;line-height:24px;color:var(--muted)}
.about .pic{position:absolute;top:82px;width:236px;height:236px;border-radius:50%}
.pic-a{left:598px;background:radial-gradient(circle at 50% 40%,#8c8e86,#5f6a4b 70%)}
.pic-b{left:864px;background:radial-gradient(circle at 50% 40%,#a3ad86,#5c7a3b 70%)}

/* events band */
.events-band{top:1000px;height:476px;background:linear-gradient(120deg,#0b3f8c,#1561b7 60%,#0b4aa0)}
.calendar{position:absolute;left:86px;top:40px;width:602px;height:398px;background:#fff;border-radius:4px;font-family:"Montserrat",Arial,sans-serif}
.cal-top{position:absolute;top:36px;left:0;right:0;display:flex;justify-content:space-between;padding:0 48px;align-items:center;color:var(--navy)}
.cal-top .yr{font-size:13px;font-weight:600}
.cal-top .month{font-size:22px;color:#555;letter-spacing:.5px}
.cal-grid{position:absolute;left:52px;top:116px;width:500px;display:grid;grid-template-columns:repeat(7,1fr);row-gap:19px;text-align:center;font-size:13px;color:#222}
.cal-grid .dow{font-size:17px;font-weight:500;margin-bottom:8px}
.cal-grid .today span{display:inline-block;width:26px;height:26px;line-height:26px;border-radius:50%;background:var(--teal);color:#fff;margin-top:-5px}
.cal-arrow{position:absolute;top:238px}
.events{position:absolute;left:720px;top:44px;width:392px;color:#fff}
.events-head{display:flex;justify-content:space-between;align-items:center;height:30px}
.events-head h3{font-size:22px;font-weight:500}
.events-head .ctrl{display:flex;gap:6px}
.event{display:flex;gap:22px;padding:24px 0 22px;border-bottom:1px solid rgba(255,255,255,.25)}
.event:last-child{border-bottom:0}
.event-date{flex:none;width:66px;height:66px;border:2px solid #fff;border-radius:50%;text-align:center;font-family:"Montserrat",Arial,sans-serif;padding-top:10px}
.event-date b{display:block;font-size:22px;font-weight:500;line-height:24px}
.event-date small{font-size:11px}
.event h4{font-size:12px;font-weight:600;margin-top:4px}
.event p{font-size:11.5px;line-height:23px;margin-top:8px;opacity:.9}

/* training */
.training{top:1476px;height:504px;text-align:center}
.training h2{margin-top:46px;color:var(--navy);font-size:25px;font-weight:500;letter-spacing:.5px}
.training .lede{margin-top:16px;font-size:11.5px;color:var(--muted)}
.resources{display:flex;gap:80px;justify-content:center;margin-top:40px}
.resource{width:180px;display:flex;flex-direction:column;align-items:center}
.resource .pic{width:184px;height:184px;border-radius:50%;border:3px solid #fff;box-shadow:0 0 0 1px #ccc}
.resource h4{color:var(--teal);font-size:13.5px;font-weight:600;margin-top:24px;white-space:nowrap}
.resource p{font-size:11.5px;line-height:25px;color:var(--muted);margin-top:10px;width:220px}

/* sign-in banner */
.signin{top:1980px;height:404px;background:linear-gradient(100deg,#4f6a33 0%,#6e8a45 40%,#9ba78a 60%,#3f5b74 100%)}
.signin-disc{position:absolute;left:150px;top:26px;width:412px;height:412px;border-radius:50%;background:rgba(23,160,134,.88);color:#fff;text-align:center;padding-top:82px}
.signin-disc h3{font-size:20px;font-weight:500;letter-spacing:.5px;font-family:"Montserrat",Arial,sans-serif}
.signin-disc p{font-size:11.5px;line-height:25px;margin:14px auto 0;width:270px}
.signin-actions{display:flex;gap:8px;justify-content:center;margin-top:26px}
.signin-actions .btn{height:38px;line-height:38px;font-size:11.5px;font-weight:700;padding:0 10px}
.btn-member{background:var(--navy);width:124px}
.btn-club{background:var(--sky);width:122px}

/* newsletter */
.newsletter{top:2384px;height:302px;background:var(--mist);text-align:center}
.newsletter h2{margin-top:50px;color:var(--navy);font-size:25px;font-weight:500;letter-spacing:.5px}
.newsletter p{margin-top:20px;font-size:11.5px;line-height:24px;color:var(--muted)}
.subscribe{display:flex;width:730px;margin:32px auto 0;height:48px}
.subscribe .field{flex:1;background:#fff;border:1px solid #e0e0e0;text-align:left;padding-left:14px;line-height:46px;font-size:11px;color:#444}
.subscribe .btn{width:136px;background:var(--navy);line-height:48px;font-size:13px;font-weight:600}

/* footer */
.site-footer{top:2686px;height:309px;background:var(--coal);color:#fff}
.footer-brand{position:absolute;top:0;left:0;right:0;height:108px;display:flex;justify-content:center;align-items:center;gap:14px;font-size:28px;font-weight:600;border-bottom:1px solid #444;margin:0 86px}
.footer-brand .brand-dot{width:22px;height:22px}
.contacts{position:absolute;top:108px;left:86px;right:86px;height:126px;border-bottom:1px solid #444;display:flex;justify-content:space-between;align-items:center;padding:0 28px}
.contact{display:flex;gap:16px;align-items:flex-start}
.contact .ico{width:54px;height:54px;border:1.5px solid #ccc;border-radius:50%;display:flex;align-items:center;justify-content:center;flex:none}
.contact h4{font-size:17px;font-weight:500;margin-top:4px}
.contact p{font-size:11px;line-height:21px;color:#ddd}
.copyright{position:absolute;bottom:24px;left:0;right:0;text-align:center;font-size:11px;color:#ddd}
</style>
</head>
<body>
<div class="canvas">

<header class="site-header">
  <div class="brand"><span class="brand-dot"></span>MARLOWE LAWN SPORTS GUILD</div>
  <nav class="nav">
    <a href="#">HOME</a><a href="#">ABOUT</a><a href="#">HOW TO PLAY</a><a href="#">NEWSLETTER</a><a href="#">CLUB NEWS</a><a href="#">EVENTS</a><a href="#">MORE</a><a href="#" class="join">JOIN CROQUET CLUB</a>
  </nav>
</header>

<section class="hero">
  <div class="photo" role="img" aria-label="Four croquet players in hats and sportswear standing on a lawn"></div>
  <div class="hero-copy">
    <h1>MARLOWE LAWN SPORTS GUILD</h1>
    <p>THE OFFICIAL SITE OF MARLOWE LAWN SPORTS GUILD INC</p>
    <a href="#" class="btn">DOWNLOADS</a>
  </div>
</section>

<section class="about">
  <h2>ABOUT OUR COMPANY</h2>
  <p>Croquet is a very old game that had its beginnings in the early 1400's. Below is a brief history of the game. England developed the initial rules of the game in the mid 1800's and the game is now played in about 26 countries around the world. Australia was an early adopter of the game and now has about 8,000 players of which just under 3,000 are in NSW. Since its early beginnings, croquet has evolved into 5 different codes and the rules formalised to provide the modern games.Croquet is a game that can be 10 but it is an ideal game for those in the senior age group.</p>
  <div class="pic pic-a" role="img" aria-label="Two players shaking hands on the croquet lawn"></div>
  <div class="pic pic-b" role="img" aria-label="A player bending over a mallet and balls on the lawn"></div>
</section>

<section class="events-band">
  <div class="calendar">
    <div class="cal-top"><span class="yr">2017</span><span class="month">JUNE, 2018</span><span class="yr">2019</span></div>
    <svg class="cal-arrow" style="left:10px" width="18" height="18" viewBox="0 0 18 18"><circle cx="9" cy="9" r="8" fill="none" stroke="#888"/><path d="M10.5 5.5 7 9l3.5 3.5" fill="none" stroke="#888" stroke-width="1.5"/></svg>
    <svg class="cal-arrow" style="right:10px" width="18" height="18" viewBox="0 0 18 18"><circle cx="9" cy="9" r="8" fill="none" stroke="#888"/><path d="M7.5 5.5 11 9l-3.5 3.5" fill="none" stroke="#888" stroke-width="1.5"/></svg>
    <div class="cal-grid">
      <div class="dow">SUN</div><div class="dow">MON</div><div class="dow">TUE</div><div class="dow">WED</div><div class="dow">THUR</div><div class="dow">FRI</div><div class="dow">SAT</div>
      <div>1</div><div>2</div><div>3</div><div>4</div><div>5</div><div>6</div><div>7</div>
      <div>8</div><div class="today"><span>9</span></div><div>10</div><div>11</div><div>12</div><div>13</div><div>14</div>
      <div>15</div><div>16</div><div>17</div><div>18</div><div>19</div><div>20</div><div>21</div>
      <div>22</div><div>23</div><div>24</div><div>25</div><div>26</div><div>27</div><div>28</div>
      <div>29</div><div>30</div><div>31</div>
    </div>
  </div>
  <div class="events">
    <div class="events-head">
      <h3>SPECIAL EVENTS</h3>
      <div class="ctrl">
        <svg width="24" height="24" viewBox="0 0 24 24"><circle cx="12" cy="12" r="11" fill="none" stroke="#fff" stroke-width="1.5"/><path d="M13.5 8 9.5 12l4 4" fill="none" stroke="#fff" stroke-width="1.8"/></svg>
        <svg width="24" height="24" viewBox="0 0 24 24"><circle cx="12" cy="12" r="11" fill="none" stroke="#fff" stroke-width="1.5"/><path d="M10.5 8l4 4-4 4" fill="none" stroke="#fff" stroke-width="1.8"/></svg>
      </div>
    </div>
    <div class="event"><div class="event-date"><b>05</b><small>JUN</small></div><div><h4>GUILD HEADQUARTERS</h4><p>A Members Area can now be accessed after sign in, to contain items less suitable for public access.</p></div></div>
    <div class="event"><div class="event-date"><b>15</b><small>JUN</small></div><div><h4>THE GC GUILD MEN'S SINGLES CHAMPIONSHIP</h4><p>A decision has also been made on a way forward for the Ferndale site, and progress has been made</p></div></div>
    <div class="event"><div class="event-date"><b>28</b><small>JUN</small></div><div><h4>SCHEDULE OF FEES AND REIMBURSABLES</h4><p>Club competitions are events held within a club, such as club championships. Clubs should add</p></div></div>
  </div>
</section>

<section class="training">
  <h2>TRAINING RESOURCES</h2>
  <p class="lede">Croquet is a very old game that had its beginnings in the early 1400's. Below is a brief history of the game</p>
  <div class="resources">
    <div class="resource"><div class="pic" role="img" aria-label="Players gathered under a marquee at headquarters" style="background:linear-gradient(180deg,#8fb2cf,#4f6b3a)"></div><h4>HEADQUARTERS</h4><p>Croquet is a very old game that had its beginnings in the early 1400's. Below is a brief history of the game</p></div>
    <div class="resource"><div class="pic" role="img" aria-label="Two singles champions standing together" style="background:linear-gradient(180deg,#6d8a4e,#c9c6bd)"></div><h4>SINGLES CHAMPIONSHIP</h4><p>Croquet is a very old game that had its beginnings in the early 1400's. Below is a brief history of the game</p></div>
    <div class="resource"><div class="pic" role="img" aria-label="Group of players holding a welcome banner" style="background:linear-gradient(180deg,#4a6a3c,#d8d8dd)"></div><h4>HEADQUARTERS</h4><p>Croquet is a very old game that had its beginnings in the early 1400's. Below is a brief history of the game</p></div>
    <div class="resource"><div class="pic" role="img" aria-label="Division 2 pennant team with a banner" style="background:linear-gradient(180deg,#3d4a3a,#e2e2e2)"></div><h4>DIVISION 2 PENNANTS</h4><p>Croquet is a very old game that had its beginnings in the early 1400's. Below is a brief history of the game</p></div>
  </div>
</section>

<section class="signin" role="img" aria-label="A player leaning over a mallet on a green lawn beside shrubs and a parked car">
  <div class="signin-disc">
    <h3>MARLOWE LAWN SPORTS GUILD</h3>
    <p>The May MLSG Board update for Members has been released, with interesting news on the succe but two sports development grants.</p>
    <div class="signin-actions"><a href="#" class="btn btn-member">MEMBER SIGN IN</a><a href="#" class="btn btn-club">CLUB SIGN</a></div>
  </div>
</section>

<section class="newsletter">
  <h2>OUR NEWSLETTER</h2>
  <p>Initially this contains MLSG Meeting Minutes, which will be removed from the Governance page in due course,<br>and other content will be moved to the Members Area shortly.</p>
  <div class="subscribe"><div class="field">Enter Your Email :</div><a href="#" class="btn">SUBMIT</a></div>
</section>

<footer class="site-footer">
  <div class="footer-brand brand"><span class="brand-dot"></span>MARLOWE LAWN SPORTS GUILD</div>
  <div class="contacts">
    <div class="contact">
      <div class="ico"><svg width="18" height="22" viewBox="0 0 18 22"><path d="M9 1a7 7 0 0 0-7 7c0 5 7 13 7 13s7-8 7-13a7 7 0 0 0-7-7z" fill="#fff"/><circle cx="9" cy="8" r="2.6" fill="#262626"/></svg></div>
      <div><h4>Address :</h4><p>Marlowe Lawn Sports Guild Inc. P.O. Box 4821<br>Ashbury Vale NSW 1490</p></div>
    </div>
    <div class="contact">
      <div class="ico"><svg width="18" height="14" viewBox="0 0 18 14"><rect x="1" y="1" width="16" height="12" fill="none" stroke="#fff" stroke-width="1.5"/><path d="M1 1l8 7 8-7" fill="none" stroke="#fff" stroke-width="1.5"/></svg></div>
      <div><h4>Email</h4><p>info@marlowe-guild.org</p></div>
    </div>
    <div class="contact">
      <div class="ico"><svg width="18" height="18" viewBox="0 0 24 24"><path d="M6.6 10.8a15 15 0 0 0 6.6 6.6l2.2-2.2c.3-.3.7-.4 1-.2 1.1.4 2.3.6 3.6.6.6 0 1 .4 1 1V20c0 .6-.4 1-1 1A17 17 0 0 1 3 4c0-.6.4-1 1-1h3.5c.6 0 1 .4 1 1 0 1.3.2 2.5.6 3.6.1.3 0 .7-.2 1z" fill="#fff"/></svg></div>
      <div><h4>Phone</h4><p>Mobile : (02) 5550 1837</p></div>
    </div>
  </div>
  <p class="copyright">© Copyright-2018 Marlowe Lawn Sports Guild All rights reserved.</p>
</footer>

</div>
</body>
</html>
```